One page template design

Hi creative designer, I want one single page template to use on my newly formed company.

The design most be built around the company logo (see lorvenmix.com) and I would like to focus this layout around the top bar and the footer. The middle should be simple and clean for I need to use it with different pages with different functionalities.

The homepage will be used to promote services but on the footer I will place links to our online tools and future internal projects and documentations.

For the homepage I'd like to see well aligned boxes where the products and services will be places. Each project will have a logo (which you don't need to design, but the page layout should have spaces to put them on).

Many thanks.

```html
<!DOCTYPE html>
<html lang="en">
<head>
<meta charset="utf-8">
<title>Lorvenmix.com – Best, Smart &amp; Effective Solutions</title>
<link rel="stylesheet" href="https://fonts.googleapis.com/css2?family=Ubuntu:ital,wght@0,500;0,700;1,700&family=Arimo:wght@400;700&display=swap">
<style>
  :root {
    --brand-blue: #0a8bbd;
    --brand-blue-dark: #0b7fae;
    --band-blue: #0e8fc2;
    --band-light: #47b0d8;
    --accent-red: #d91b46;
    --text-dark: #1f1f1f;
    --text-body: #555555;
    --panel-white: #ffffff;
    --box-border: #d9d9d9;
    --box-head-top: #fbfbfb;
    --box-head-bottom: #e6e6e6;
    --footer-grey: #d8d8d8;
    --footer-blue: #0b8dc0;
    --footer-text: #ffffff;
  }
  * { margin: 0; padding: 0; box-sizing: border-box; }
  html, body { width: 1200px; height: 865px; overflow: hidden; background: #ffffff; }
  body { position: relative; font-family: "Arimo", Arial, sans-serif; }

  .site-header {
    position: absolute; left: 0; top: 0; width: 1200px; height: 114px;
    background: linear-gradient(#ffffff, #f3f3f3);
    border-bottom: 1px solid #e2e2e2;
  }
  .brand {
    position: absolute; left: 80px; top: 24px; height: 58px;
    display: flex; align-items: center; gap: 14px;
  }
  .brand-dot { width: 44px; height: 44px; border-radius: 50%; background: var(--accent-red); }
  .brand-name {
    font-family: "Ubuntu", sans-serif; font-weight: 700; font-size: 40px;
    color: var(--brand-blue); letter-spacing: -0.5px;
  }
  .main-nav {
    position: absolute; right: 96px; top: 47px; height: 26px;
    display: flex; align-items: center; font-size: 15.5px; color: var(--brand-blue-dark);
  }
  .main-nav a { color: var(--brand-blue-dark); text-decoration: none; }
  .main-nav .sep { margin: 0 13px; }
  .main-nav .current {
    background: var(--brand-blue); color: #ffffff; border-radius: 13px;
    padding: 4px 17px; margin-right: 20px; box-shadow: 0 2px 2px rgba(0,0,0,.2);
  }

  .hero-band { position: absolute; left: 0; top: 115px; width: 1200px; height: 201px; background: var(--band-blue); }
  .hero-band svg { display: block; }

  .content-panel {
    position: absolute; left: 83px; top: 152px; width: 1020px; height: 632px;
    background: var(--panel-white); border-radius: 8px 8px 0 0;
    box-shadow: 0 0 40px rgba(0,0,0,.22);
  }
  .hero-photo {
    position: absolute; left: 505px; top: 5px; width: 512px; height: 252px; z-index: 1;
    background: linear-gradient(90deg, rgba(255,255,255,1) 0%, #d9dde2 25%, #b8c4cf 55%, #e9e4df 80%, #f6f3f0 100%);
  }
  .intro { position: absolute; left: 39px; top: 31px; width: 490px; z-index: 2; }
  .intro-title {
    font-family: "Ubuntu", sans-serif; font-style: italic; font-weight: 700;
    font-size: 31px; line-height: 32px;
  }
  .intro-title .line-one { color: var(--brand-blue); display: block; }
  .intro-title .line-two { color: var(--accent-red); display: block; }
  .intro-text { margin-top: 15px; font-size: 15px; line-height: 21.6px; color: var(--text-dark); }

  .service-grid { position: absolute; left: 26px; top: 276px; display: flex; gap: 16px; }
  .service-card {
    width: 232px; height: 288px; border: 1px solid var(--box-border); border-radius: 5px;
    background: #ffffff; position: relative; overflow: hidden;
  }
  .service-head {
    height: 43px; border-bottom: 1px solid var(--box-border);
    background: linear-gradient(var(--box-head-top), var(--box-head-bottom));
    padding: 12px 0 0 13px;
    font-size: 16.5px; font-weight: 700; color: var(--brand-blue-dark);
  }
  .service-logo {
    margin: 4px auto 0; width: 156px; height: 96px; border-radius: 6px;
    background: radial-gradient(ellipse at center, #9fd3ec 0%, #dbeff8 55%, #ffffff 80%);
  }
  .service-text {
    margin: 6px 13px 0; font-size: 14px; line-height: 17.4px; color: var(--text-body);
    text-align: justify; height: 87px; overflow: hidden;
  }
  .read-more {
    position: absolute; left: 12px; top: 249px; width: 102px; height: 23px;
    border: 1px solid #c9c9c9; border-radius: 12px;
    background: linear-gradient(#ffffff, #e9e9e9); box-shadow: 0 2px 2px rgba(0,0,0,.15);
    font-size: 12px; color: #777777; text-align: center; line-height: 21px; text-decoration: none;
  }

  .footer-strip { position: absolute; left: 0; top: 794px; width: 1200px; height: 14px; background: var(--footer-grey); }
  .site-footer {
    position: absolute; left: 0; top: 808px; width: 1200px; height: 57px; background: var(--footer-blue);
    color: var(--footer-text);
  }
  .copyright { position: absolute; left: 88px; top: 12px; font-size: 14.4px; }
  .footer-nav { position: absolute; right: 93px; top: 14px; font-size: 15px; display: flex; }
  .footer-nav a { color: var(--footer-text); text-decoration: none; }
  .footer-nav .sep { margin: 0 11px; }
</style>
</head>
<body>
  <header class="site-header">
    <div class="brand">
      <span class="brand-dot"></span>
      <span class="brand-name">Lorvenmix.com</span>
    </div>
    <nav class="main-nav">
      <a class="current" href="#">Home</a>
      <a href="#">Web Design</a><span class="sep">|</span>
      <a href="#">Web Development</a><span class="sep">|</span>
      <a href="#">Web Hosting</a><span class="sep">|</span>
      <a href="#">Domain Registration</a>
    </nav>
  </header>

  <div class="hero-band">
    <svg width="1200" height="201" viewBox="0 0 1200 201">
      <path d="M0 0 H420 C300 40 140 110 0 180 Z" fill="var(--band-light)" opacity=".55"/>
      <path d="M0 0 H260 C170 40 80 80 0 110 Z" fill="#6cc2e3" opacity=".5"/>
      <path d="M760 0 H1200 V70 C1080 30 920 10 760 0 Z" fill="var(--band-light)" opacity=".45"/>
    </svg>
  </div>

  <main class="content-panel">
    <div class="hero-photo" role="img" aria-label="Photo of a smiling businesswoman giving a thumbs up with cheering colleagues behind her"></div>
    <section class="intro">
      <h1 class="intro-title">
        <span class="line-one">Best, Smart &amp;</span>
        <span class="line-two">Effective Solutions</span>
      </h1>
      <p class="intro-text">Lorem ipsum dolor sit amet, consectetur adipiscing elit. Donec commodo aliquet orci, nec sollicitudin eros lacinia sed. Morbi hendrerit mi et arcu volutpat in dictum leo egestas. Aliquam tristique odio in elit lobortis porttitor. In egestas quam id sapien ultricies rhoncus placerat lorem rutrum. Quisque non quam in leo consectetur dignissim nec ac risus. Aliquam elementum lacus et leo dapibus porttitor.</p>
    </section>

    <section class="service-grid">
      <article class="service-card">
        <h2 class="service-head">XML Debugger</h2>
        <div class="service-logo" role="img" aria-label="Illustration of a globe connected to networked figures"></div>
        <p class="service-text">Morbi iaculis dolor quis sapien fringilla vol theutpat. Vestibulum a quam purus. Sed magna sem, ullamco rper id condimentum ac, imperdiet in lorem.</p>
        <a class="read-more" href="#">read more ›</a>
      </article>
      <article class="service-card">
        <h2 class="service-head">Reciprocal links</h2>
        <div class="service-logo" role="img" aria-label="Illustration of figures linked around a central hub"></div>
        <p class="service-text">Morbi iaculis dolor quis sapien fringilla vol theutpat. Vestibulum a quam purus. Sed magna sem, ullamco rper id condimentum ac, imperdiet in lorem.</p>
        <a class="read-more" href="#">read more ›</a>
      </article>
      <article class="service-card">
        <h2 class="service-head">IT Sources</h2>
        <div class="service-logo" role="img" aria-label="Illustration of figures assembling puzzle pieces"></div>
        <p class="service-text">Morbi iaculis dolor quis sapien fringilla vol theutpat. Vestibulum a quam purus. Sed magna sem, ullamco rper id condimentum ac, imperdiet in lorem.</p>
        <a class="read-more" href="#">read more ›</a>
      </article>
      <article class="service-card">
        <h2 class="service-head">Start Crawling</h2>
        <div class="service-logo" role="img" aria-label="Illustration of a hierarchy of connected figures"></div>
        <p class="service-text">Morbi iaculis dolor quis sapien fringilla vol theutpat. Vestibulum a quam purus. Sed magna sem, ullamco rper id condimentum ac, imperdiet in lorem.</p>
        <a class="read-more" href="#">read more ›</a>
      </article>
    </section>
  </main>

  <div class="footer-strip"></div>
  <footer class="site-footer">
    <p class="copyright">©2009-2010 Lorvenmix.com - All Rights Reserved</p>
    <nav class="footer-nav">
      <a href="#">Home</a><span class="sep">|</span>
      <a href="#">Web Design</a><span class="sep">|</span>
      <a href="#">Web Development</a><span class="sep">|</span>
      <a href="#">Web Hosting</a><span class="sep">|</span>
      <a href="#">Domain Registration</a>
    </nav>
  </footer>
</body>
</html>
```